Crestline Marketing Business Card

Business card using new logo for marketing consulting company based in Silicon Valley. Limited information on card now (name, phone number, email, website), but room to add mailing address later.

```html
<!DOCTYPE html>
<html lang="en">
<head>
<meta charset="UTF-8">
<title>Crestline Marketing Business Card</title>
<link href="https://fonts.googleapis.com/css2?family=Open+Sans:wght@400&family=Tinos:wght@400;700&display=swap" rel="stylesheet">
<style>
  :root {
    --paper: #ffffff;
    --ink: #000000;
    --brand-cyan: #1ebfee;
    --brand-navy: #1b2c52;
    --label-grey: #7a7a7a;
  }
  html, body {
    margin: 0;
    padding: 0;
    width: 828px;
    height: 1200px;
    overflow: hidden;
    background: var(--paper);
  }
  .sheet {
    position: relative;
    width: 828px;
    height: 1200px;
  }
  .card {
    position: absolute;
    box-sizing: border-box;
    border: 2px solid var(--ink);
    background: var(--paper);
  }
  .card--front { left: 43px; top: 31px; width: 737px; height: 424px; }
  .card--back  { left: 43px; top: 614px; width: 745px; height: 425px; }

  .side-caption {
    position: absolute;
    left: 0;
    width: 828px;
    text-align: center;
    font-family: "Tinos", "Times New Roman", serif;
    font-size: 33px;
    letter-spacing: 1px;
    color: var(--ink);
    margin: 0;
  }
  .side-caption--front { top: 480px; }
  .side-caption--back  { top: 1078px; }

  .brand-dot {
    position: absolute;
    border-radius: 50%;
    background: var(--brand-cyan);
  }
  .brand-name {
    position: absolute;
    margin: 0;
    font-family: "Open Sans", Arial, sans-serif;
    font-weight: 400;
    color: var(--brand-cyan);
    white-space: nowrap;
    text-align: center;
  }
  .card--front .brand-dot { left: 134px; top: 64px; width: 104px; height: 104px; }
  .card--front .brand-name { left: 50px; top: 180px; width: 272px; font-size: 26px; }
  .card--back .brand-dot { left: 301px; top: 84px; width: 150px; height: 150px; }
  .card--back .brand-name { left: 0; top: 264px; width: 741px; font-size: 48px; }

  .field {
    position: absolute;
    margin: 0;
    font-family: "Tinos", "Times New Roman", serif;
    font-size: 18px;
    white-space: nowrap;
  }
  .field--name   { left: 359px; top: 238px; color: var(--brand-cyan); font-weight: 700; }
  .field--tel    { left: 67px;  top: 306px; color: var(--brand-navy); font-weight: 700; }
  .field--web    { left: 68px;  top: 343px; color: var(--label-grey); font-weight: 400; }
  .field--email  { left: 476px; top: 306px; color: var(--brand-navy); font-weight: 700; }
  .field--address{ left: 476px; top: 342px; color: var(--label-grey); font-weight: 400; }
</style>
</head>
<body>
<main class="sheet">
  <section class="card card--front" aria-label="Front side of business card">
    <span class="brand-dot" aria-hidden="true"></span>
    <p class="brand-name">Crestline Marketing</p>
    <p class="field field--name">Name:</p>
    <p class="field field--tel">Tel.:</p>
    <p class="field field--web">Web:</p>
    <p class="field field--email">E-mail:</p>
    <p class="field field--address">Adress:</p>
  </section>
  <p class="side-caption side-caption--front">FRONT SIDE</p>

  <section class="card card--back" aria-label="Back side of business card">
    <span class="brand-dot" aria-hidden="true"></span>
    <p class="brand-name">Crestline Marketing</p>
  </section>
  <p class="side-caption side-caption--back">BACK SIDE</p>
</main>
</body>
</html>
```